brindlecove.com website design (promote tax and financial services)

I need web design layouts for a 4-6 page website for a finance and tax services business.

Assumptions:
-Responsive design for desktop, laptop, tablet and mobile
-website will not be programmed with any flash elements
-Animation is welcomed
-stock photography may be required (royalty free preferred)
-Prefer to stay away from designs with large images that result in long loading times
-Web design will be pulled through to other digital and print promotional materials that the company develops

The audience is primarily male. Attached is the site and content map, including the company logo

Target Market(s)

individuals and small-to-medium business owners
Primary geographic market = NYC metropolitan area
Secondary geographic market = East Coast USA
Tertiary geographic market = National USA

Any stock photography should represent a diverse population

Industry/Entity Type

Financial Service

Number of Pages Required

5+ page

Font styles to use
Sans Serif

Colors
0758a4
9bcb3b

Requirements
Must have
• -Responsive design that translates nicely to mobile and tablet devices
• -Simple, clean but yet sophisticated design
• -Be in alignment with or a derivative of the logo design (provided with PPT attachment)
• -Compatibility with website programming and coding software
• -Include a countdown to the tax deadline (April 18, 2016)
• -Web-friendly fonts
• -Search box
• -Link to social media properties (via social icons)
• -Include company phone number and clickable link to activate ability to contact company by email
Nice to have
• -Simple animation, as long as it does not impact load time
• -Engaging call-to-action buttons
• -Rotating homepage banners
• -Original icons
• -"About Us" page should have a friendlier, welcoming design
• -Image/Photo caption examples
• -Assume that copy (text) can be minimized to accommodate more visual displays
• -"Continue reading" or "read more" links to expand truncated copy are welcomed
• -A pricing table (not a priority, but nice to have)
Should not have
• Overcrowded design (don't be afraid of white space, if needed)
• too many bells and whistles (flash animation, moving cursors etc.)

```html
<!DOCTYPE html>
<html lang="en">
<head>
<meta charset="utf-8">
<title>brindlecove.com – Tax Preparation</title>
<link rel="stylesheet" href="https://fonts.googleapis.com/css2?family=Roboto:wght@300;400;500;700&display=swap">
<style>
:root{
  --blue:#0b5cad;
  --blue-dark:#074c91;
  --green:#14a04a;
  --green-light:#1fb65a;
  --orange:#f98a33;
  --ink:#333;
  --muted:#666;
  --line:#e3e3e3;
  --dark:#262626;
  --white:#fff;
}
*{box-sizing:border-box;margin:0;padding:0}
html,body{width:1200px;height:4934px;overflow:hidden}
body{font-family:'Roboto',sans-serif;color:var(--ink);background:var(--white);position:relative}
section,header,footer{position:relative;width:1200px;overflow:hidden}
.center{text-align:center}

/* header */
.site-header{height:94px;display:flex;align-items:center;padding:0 80px 0 100px;border-bottom:1px solid #eee}
.brand{display:flex;align-items:center;gap:10px;font-size:20px;font-weight:700;color:var(--blue)}
.brand-square{width:22px;height:22px;background:var(--blue)}
.main-nav{display:flex;align-items:center;gap:36px;margin-left:auto;font-size:13px;color:#777}
.main-nav .active{color:var(--blue)}
.main-nav .phone{color:var(--green);text-decoration:underline}
.search{width:36px;height:36px;border:1px solid #ccc;border-radius:50%;display:flex;align-items:center;justify-content:center}

/* hero */
.hero{height:559px;color:var(--white)}
.hero-photo{position:absolute;inset:0;background:linear-gradient(120deg,#3b4651 0%,#6e7b86 45%,#4c5a63 70%,#2b3237 100%)}
.hero-shade{position:absolute;inset:0;background:rgba(20,30,40,.45)}
.hero-body{position:absolute;left:0;right:0;top:148px}
.hero-kicker{font-size:20px;font-weight:400}
.hero-title{font-size:40px;font-weight:700;margin-top:6px}
.hero-lede{font-size:13px;margin-top:10px}
.btn-green{display:inline-block;background:var(--green);color:#fff;border:2px solid #fff;border-radius:3px;font-size:14px;font-weight:500;padding:11px 22px}
.hero .btn-green{margin-top:20px}
.hero-email{font-size:14px;margin-top:10px}
.hero-why{font-size:19px;font-weight:700;margin-top:26px}
.hero-note{font-size:13px;margin-top:14px}
.slide-arrow{position:absolute;top:355px;width:30px;height:30px;border-radius:50%;background:rgba(0,0,0,.3);display:flex;align-items:center;justify-content:center}

/* headings */
.section-title{font-size:29px;font-weight:400;letter-spacing:.5px}
.title-rule{width:72px;height:3px;background:var(--blue);margin:22px auto 0}

/* services */
.services{height:660px;padding-top:78px}
.services .section-title{color:var(--blue)}
.service-cards{position:absolute;top:165px;left:124px;display:flex;gap:4px}
.card{position:relative;width:314px;height:419px;color:#fff;text-align:center;padding:28px 30px 0;overflow:hidden}
.card.blue{background:var(--blue)}
.card.green{background:var(--green)}
.card-icon{width:107px;height:107px;border-radius:50%;border:4px solid var(--green-light);background:#fff;margin:0 auto;display:flex;align-items:center;justify-content:center}
.card.green .card-icon{border-color:#fff;background:var(--green)}
.card h3{font-size:20px;font-weight:400;margin-top:30px}
.card p{font-size:12px;line-height:21px;margin-top:14px}
.btn-outline{display:inline-block;border:1px solid #fff;font-size:11px;padding:8px 24px;margin-top:26px}
.card-wave{position:absolute;left:0;bottom:0;width:314px;height:80px}

/* story */
.story{height:540px;color:#fff}
.story-photo{position:absolute;inset:0;background:radial-gradient(ellipse at 50% 40%,#7a6a5e 0%,#4c4a4a 45%,#2f3133 100%)}
.story-shade{position:absolute;inset:0;background:rgba(15,15,15,.5)}
.story-body{position:absolute;top:122px;left:214px;width:774px;text-align:center}
.story-body h2{font-size:40px;font-weight:400}
.story-body p{font-size:12px;line-height:21px;margin-top:16px}
.story-body .ask{font-size:13px;margin-top:30px}

/* testimonials */
.testimonials{height:650px;padding-top:77px}
.testimonials .lede{font-size:15px;line-height:22px;color:var(--muted);width:640px;margin:10px auto 0}
.referral{position:absolute;top:2191px;transform:translate(-50%,-50%);width:300px;height:300px;border:2px dashed #ccc;border-radius:50%;display:flex;align-items:center;justify-content:center;background:#fff}
.referral-inner{width:276px;height:276px;border-radius:50%;color:#fff;text-align:center;padding-top:54px}
.referral.g .referral-inner{background:var(--green)}
.referral.o .referral-inner{background:var(--orange)}
.referral .count{font-size:17px;margin-top:12px}
.referral .save{font-size:32px;font-weight:700;margin-top:8px}
.referral .fee{font-size:16px;margin-top:6px}
.referral .cap{font-size:10px;margin-top:4px}
.referral-shadow{position:absolute;top:2367px;width:180px;height:14px;border-radius:50%;background:radial-gradient(ellipse,rgba(0,0,0,.18),rgba(0,0,0,0) 70%);transform:translateX(-50%)}
.btn-deal{position:absolute;top:2411px;left:522px;width:156px;height:40px;border:2px solid var(--blue);border-radius:3px;color:var(--blue);font-size:15px;display:flex;align-items:center;justify-content:center}

/* convenience band */
.convenience{height:379px;color:#fff}
.convenience-photo{position:absolute;inset:0;background:linear-gradient(110deg,#1b8e48 0%,#2cb866 40%,#1ea055 70%,#13843f 100%)}
.convenience-body{position:absolute;top:112px;left:0;right:0;text-align:center}
.convenience-body h2{font-size:37px;font-weight:400}
.convenience-body p{font-size:19px;line-height:26px;margin-top:14px}

/* faq */
.faq{height:624px;padding-top:70px}
.faq .lede{font-size:15px;line-height:22px;color:var(--muted);width:640px;margin:10px auto 0}
.faq-list{position:absolute;top:171px;left:193px;width:812px}
.faq-item{display:flex;height:52px;border:1px solid var(--line);border-top:none;align-items:center;font-size:12px;color:#777}
.faq-item .q{flex:1;padding-left:16px}
.faq-toggle{width:46px;height:100%;background:var(--green);color:#fff;font-size:22px;display:flex;align-items:center;justify-content:center}
.faq-item.open{background:#6e6e6e;color:#fff;border:none;height:39px}
.faq-answer{border:1px solid var(--line);border-top:none;padding:22px 20px;font-size:11px;line-height:20px;color:#777;height:103px}

/* countdown */
.countdown{height:444px;color:#fff}
.countdown-photo{position:absolute;inset:0;background:linear-gradient(135deg,#2b2d31 0%,#1c1e22 55%,#3a3c40 100%)}
.countdown-body{position:absolute;top:76px;left:0;right:0;text-align:center}
.countdown-body .t1{font-size:30px;font-weight:400}
.countdown-body .t2{font-size:41px;font-weight:400;margin-top:4px}
.timer{display:flex;justify-content:center;gap:23px;margin-top:32px}
.timer-box{width:123px;height:135px;border:1px solid rgba(255,255,255,.4)}
.timer-num{height:70px;background:var(--green);font-size:48px;display:flex;align-items:center;justify-content:center;position:relative}
.timer-label{height:65px;background:var(--blue);font-size:15px;display:flex;align-items:center;justify-content:center}
.pin{position:absolute;bottom:-8px;width:4px;height:16px;background:#fff;border-radius:2px}

/* spread */
.spread{height:199px;padding-top:62px}
.spread .section-title{color:var(--ink)}
.spread .lede{font-size:15px;line-height:22px;color:var(--muted);width:820px;margin:10px auto 0}
.spread-notch{position:absolute;bottom:0;left:548px;width:104px;height:34px}

/* forms */
.contact{height:460px;background:linear-gradient(90deg,var(--blue) 0%,var(--blue) 50%,#0a55a3 50%,var(--blue) 100%);color:#fff}
.form{position:absolute;top:52px;width:425px}
.form h3{font-size:24px;font-weight:400;margin-bottom:18px}
.field{height:36px;background:#fff;border:1px solid #ddd;font-size:11px;color:#888;padding:0 14px;display:flex;align-items:center;margin-bottom:16px}
.field.area{height:87px;align-items:flex-start;padding-top:10px}
.btn-send{width:168px;height:42px;border:2px solid #fff;border-radius:3px;font-size:16px;display:flex;align-items:center;justify-content:center;margin-top:10px}

/* footer */
.site-footer{height:325px;background:var(--dark);color:#ccc;overflow:visible}
.to-top{position:absolute;top:-28px;left:572px;width:56px;height:56px;border-radius:50%;background:var(--green);border:3px solid #fff;display:flex;align-items:center;justify-content:center}
.social{position:absolute;top:64px;left:0;right:0;display:flex;justify-content:center;gap:10px}
.social span{width:26px;height:26px;border-radius:50%;background:var(--green)}
.footer-nav{position:absolute;top:122px;left:0;right:0;display:flex;justify-content:center;gap:72px;font-size:10px}
.footer-line{position:absolute;left:0;right:0;text-align:center;font-size:10px}
.footer-brand{position:absolute;top:200px;left:0;right:0;display:flex;justify-content:center;align-items:center;gap:10px;font-size:22px;font-weight:700;color:#ccc}
.footer-brand .brand-square{background:#ccc}
</style>
</head>
<body>

<header class="site-header">
  <div class="brand"><span class="brand-square"></span>brindlecove.com</div>
  <nav class="main-nav">
    <span class="active">HOME</span><span>OUR SERVICES</span><span>OUR STORY</span><span>TESTIMONIALS</span><span>FAQ</span><span>CONTACT US</span>
    <span class="phone">Phone: (917) 555-0148</span>
    <span class="search"><svg width="14" height="14" viewBox="0 0 14 14"><circle cx="6" cy="6" r="4.2" fill="none" stroke="#333" stroke-width="1.8"/><line x1="9" y1="9" x2="13" y2="13" stroke="#333" stroke-width="1.8"/></svg></span>
  </nav>
</header>

<section class="hero">
  <div class="hero-photo" role="img" aria-label="Business people reviewing tax papers at a desk"></div>
  <div class="hero-shade"></div>
  <div class="slide-arrow" style="left:24px"><svg width="10" height="14"><path d="M8 1 2 7l6 6" fill="none" stroke="#fff" stroke-width="2"/></svg></div>
  <div class="slide-arrow" style="right:40px"><svg width="10" height="14"><path d="M2 1l6 6-6 6" fill="none" stroke="#fff" stroke-width="2"/></svg></div>
  <div class="hero-body center">
    <div class="hero-kicker">THE DEADLINE FOR FILING YOUR 2015 FEDERAL</div>
    <div class="hero-title">TAX RETURN IS APRIL 18, 2016</div>
    <div class="hero-lede">Don't wait! Set up an appointment to file your taxes now &amp; receive the most money from your tax returns</div>
    <span class="btn-green">SCHEDULE APPOINTMENT</span>
    <div class="hero-email">Email : marcus@brindlecove.com</div>
    <div class="hero-why">WHY IS TAX DAY APRIL 18?</div>
    <div class="hero-note">The federal government is observing the Washington D.C. Emancipation holiday on April 15 so Tax Day is on the following Monday</div>
  </div>
</section>

<section class="services center">
  <h2 class="section-title">OUR SERVICES</h2>
  <div class="title-rule"></div>
  <div class="service-cards">
    <div class="card blue">
      <div class="card-icon"><svg width="52" height="40" viewBox="0 0 52 40"><path d="M3 6h14l4 5h20v6H12L3 35Z M12 17h37l-9 19H3Z" fill="none" stroke="var(--blue)" stroke-width="3" stroke-linejoin="round"/></svg></div>
      <h3>Our Services &amp; Specialties</h3>
      <p>At brindlecove, we do more than simply get you prepared for tax season. We'll be with you every step of the way. Unlike some other tax preparation companies, you'll be working with the same people every year our office is small and our people remember</p>
      <svg class="card-wave" viewBox="0 0 314 80" preserveAspectRatio="none"><path d="M0 80V62C80 20 200 20 314 38V80Z" fill="#fff"/></svg>
    </div>
    <div class="card green">
      <div class="card-icon"><svg width="40" height="56" viewBox="0 0 40 56"><text x="20" y="46" text-anchor="middle" font-family="Roboto,sans-serif" font-size="52" font-weight="700" fill="#fff">$</text></svg></div>
      <h3>Save Money</h3>
      <p>Avoid any penalties that may result from filing an incorrect return. We will get all the right information from you so we can apply the proper tax rules.</p>
      <span class="btn-outline">READ MORE ➞</span>
    </div>
    <div class="card blue">
      <div class="card-icon"><svg width="40" height="46" viewBox="0 0 40 46"><path d="M4 4h32v18c0 12-8 18-16 21C12 40 4 34 4 22Z" fill="var(--blue)"/><path d="M12 10h10v24c-6-3-10-7-10-13Z" fill="#fff"/></svg></div>
      <h3>Our Promise</h3>
      <p>Taxes can be hard! Here at brindlecove, we know how to help! Our qualified experts and specialists know that your time is valuable. That's why you're here because you trust us to make the difference to put money back in your pocket. Dynamic, engaging</p>
      <svg class="card-wave" viewBox="0 0 314 80" preserveAspectRatio="none"><path d="M0 80V40C110 18 230 22 314 60V80Z" fill="#fff"/></svg>
    </div>
  </div>
</section>

<section class="story">
  <div class="story-photo" role="img" aria-label="Smiling office worker at a desk in a bright workplace"></div>
  <div class="story-shade"></div>
  <div class="story-body">
    <h2>OUR STORY</h2>
    <p>Our team is small. Our experts come from a lot of places, but we all arrived here for a reason– because we're passionate about advocating for your wallet. Our services are valuable because we offer fast resolution that puts money back in your pocket. You deserve us. We know we deserve you. Moving forward and making your taxes a stress-free process isn't hard– it's just us. It's brindlecove.</p>
    <p>Our lead specialist, Marcus, is originally from Indiana but moved to NYC shortly after graduating from Ridgefield University with a BBA in Finance. He's been the trusted tax preparer for hundreds of people and businesses, and is delighted to have to the opportunity to help you directly. We'll be with you, every step of the way.</p>
    <p class="ask">Questions? Don't hesitate to contact us. Or you can review these Frequently Asked Questions.</p>
  </div>
</section>

<section class="testimonials center">
  <h2 class="section-title">TESTIMONIALS</h2>
  <p class="lede">Take advantage of my Referral Rewards Program for even more savings. Receive a rebate on service fees with this exciting promotion!</p>
</section>

<div class="referral g" style="left:341px"><div class="referral-inner">
  <svg width="64" height="64" viewBox="0 0 64 64"><path d="M30 6A28 28 0 1 0 58 34H30Z" fill="#fff"/><path d="M35 2A28 28 0 0 1 62 29H35Z" fill="#fff"/></svg>
  <div class="count">1 REFERRAL</div><div class="save">SAVE 25%</div><div class="fee">25% off tax fees</div></div></div>
<div class="referral o" style="left:599px"><div class="referral-inner">
  <svg width="64" height="64" viewBox="0 0 64 64"><path d="M30 6A28 28 0 1 0 58 34H30Z" fill="#fff"/><path d="M35 2A28 28 0 0 1 62 29H35Z" fill="#fff"/></svg>
  <div class="count">2 REFERRALS</div><div class="save">SAVE 50%</div><div class="fee">50% off tax fees</div></div></div>
<div class="referral g" style="left:857px"><div class="referral-inner">
  <svg width="64" height="64" viewBox="0 0 64 64"><path d="M30 6A28 28 0 1 0 58 34H30Z" fill="#fff"/><path d="M35 2A28 28 0 0 1 62 29H35Z" fill="#fff"/></svg>
  <div class="count">3 REFERRALS</div><div class="save">SAVE 100%</div><div class="fee">100% off tax fees</div><div class="cap">(maximum amount = $250)</div></div></div>
<div class="referral-shadow" style="left:341px"></div>
<div class="referral-shadow" style="left:599px"></div>
<div class="referral-shadow" style="left:857px"></div>
<div class="btn-deal">DealSpark Link</div>

<section class="convenience">
  <div class="convenience-photo" role="img" aria-label="Hands working with a calculator and documents, tinted green"></div>
  <div class="convenience-body">
    <h2>FILE YOUR TAXES AT YOUR CONVENIENCE</h2>
    <p>We have early, late, and weekend appointments available upon request.<br>We will work around your schedule.</p>
  </div>
</section>

<section class="faq center">
  <h2 class="section-title">HAVE ANY QUESTIONS?</h2>
  <p class="lede">Here are some frequently asked questions. If this does not answer your question please feel free to contact us!</p>
  <div class="faq-list" style="text-align:left">
    <div class="faq-item open"><span class="q">Are you able to accommodate my busy schedule?</span><span class="faq-toggle">-</span></div>
    <div class="faq-answer">My flexible hours are designed to work around your demanding schedule, so I make myself available in the evenings and on weekends. In addition, you can choose how we work together—by phone, email, video call, or in person.</div>
    <div class="faq-item"><span class="q">How soon will you file my taxes after my initial consultation?</span><span class="faq-toggle">+</span></div>
    <div class="faq-item"><span class="q">Are you available after the April 15th tax deadline?</span><span class="faq-toggle">+</span></div>
    <div class="faq-item"><span class="q">How can I track my return?</span><span class="faq-toggle">+</span></div>
    <div class="faq-item"><span class="q">Can you manage returns with unique and/or challenging circumstances? (ie: alimony, child support, loans, education)</span><span class="faq-toggle">+</span></div>
    <div class="faq-item"><span class="q">Can I still file returns for previous years?</span><span class="faq-toggle">+</span></div>
  </div>
</section>

<section class="countdown">
  <div class="countdown-photo" role="img" aria-label="Dark desk with a laptop and a 2016 calendar"></div>
  <div class="countdown-body">
    <div class="t1">The Tax Deadline</div>
    <div class="t2">(APRIL 18, 2016)</div>
    <div class="timer">
      <div class="timer-box"><div class="timer-num">00<i class="pin" style="left:14px"></i><i class="pin" style="right:14px"></i></div><div class="timer-label">DAYS</div></div>
      <div class="timer-box"><div class="timer-num">00<i class="pin" style="left:14px"></i><i class="pin" style="right:14px"></i></div><div class="timer-label">HOURS</div></div>
      <div class="timer-box"><div class="timer-num">00<i class="pin" style="left:14px"></i><i class="pin" style="right:14px"></i></div><div class="timer-label">MINUTES</div></div>
      <div class="timer-box"><div class="timer-num">00<i class="pin" style="left:14px"></i><i class="pin" style="right:14px"></i></div><div class="timer-label">SECONDS</div></div>
    </div>
  </div>
</section>

<section class="spread center">
  <h2 class="section-title">SPREAD THE WORD, SAVE ON FILING COSTS!</h2>
  <p class="lede">Now your friends and family can also receive personalized, convenient tax preparation for maximum refunds. Make a referral and receive a rebate on your service fees. Simply fill out the form below and I'll do the rest.</p>
  <svg class="spread-notch" viewBox="0 0 104 34"><path d="M0 34 52 0l52 34Z" fill="var(--blue)"/></svg>
</section>

<section class="contact">
  <div class="form" style="left:98px">
    <h3>SEND MARCUS AN EMAIL!</h3>
    <div class="field">Subjects</div>
    <div class="field">E Mail</div>
    <div class="field">Phone No</div>
    <div class="field area">Your Message</div>
    <div class="btn-send">Send Message</div>
  </div>
  <div class="form" style="left:676px">
    <h3>SIGN UP TODAY!</h3>
    <div class="field">First Name</div>
    <div class="field">Last Name</div>
    <div class="field">E Mail</div>
    <div class="field">Phone No</div>
    <div class="field">Zip Code</div>
    <div class="btn-send">Send Message</div>
  </div>
</section>

<footer class="site-footer">
  <div class="to-top"><svg width="22" height="14" viewBox="0 0 22 14"><path d="M2 12 11 3l9 9" fill="none" stroke="#fff" stroke-width="3"/></svg></div>
  <div class="social"><span></span><span></span><span></span><span></span><span></span></div>
  <nav class="footer-nav"><span>ABOUT US</span><span>SERVICES</span><span>OUR STORY</span><span>TESTIMONIALS</span><span>FAQ</span><span>CONTACT US</span></nav>
  <div class="footer-line" style="top:154px">PHONE: (917) 555-0148.&nbsp;&nbsp; EMAIL: INFO@BRINDLECOVE.COM</div>
  <div class="footer-line" style="top:182px">© 2016. BRINDLECOVE.&nbsp;&nbsp;&nbsp;&nbsp; TERMS &nbsp;&nbsp;&nbsp;&nbsp; PRIVACY</div>
  <div class="footer-brand" style="top:218px"><span class="brand-square"></span>brindlecove.com</div>
</footer>

</body>
</html>
```